Willowmere Therapy (Endure - Renew - Flourish) - Double Sided Business Card

I would like a 2-sided business card. Front: Matte Black or Navy with Logo & Tagline. Back: Name, Address, Phone Number, Email, & Website (maybe would like to include a small map pin-pointing location); Prefer front to be a gold/silver foil (iridescent); Back prefer white or light colored background with lettering that is easy to read and simple

Target Market(s)

Individuals & Couples (13 y.o. - ALL Adults); High end clientele

Industry/Entity Type

Licensed Professional Counselor (Mental Health)

Contact Information for Business Card

Name: Willowmere Therapy; Tagline: Endure - Renew - Flourish; Address: 3175 W. Calder Ave., Suite 842, Fort Worth, TX 76142; Phone: (214) 738-2956; Website: www.WillowmereTherapy.example

Font styles to use
Serif

Requirements
Must have
• Logo on Front (Large) prefer gold/silver foil on a matte dark color (i.e. black, navy, etc.); Back of Card: All other relevant information

```html
<!DOCTYPE html>
<html lang="en">
<head>
<meta charset="utf-8">
<title>Willowmere Therapy – Business Card</title>
<link rel="stylesheet" href="https://fonts.googleapis.com/css2?family=Cinzel:wght@400&family=Montserrat:wght@400;500&family=Oswald:wght@500&display=swap">
<style>
  :root {
    --backdrop: #b0b1ac;
    --card-white: #ffffff;
    --card-black: #2a2a2a;
    --gold: #d4b44a;
    --silver: #c9c9c9;
    --text-grey: #555555;
  }
  * { box-sizing: border-box; margin: 0; padding: 0; }
  html, body { width: 1200px; height: 801px; overflow: hidden; }
  body {
    background: var(--backdrop);
    display: flex;
    align-items: center;
    justify-content: center;
    gap: 60px;
  }
  .card {
    width: 520px;
    height: 297px;
    position: relative;
    border-bottom: 4px solid var(--gold);
    box-shadow: 0 18px 30px rgba(0,0,0,0.25);
  }
  .card--back {
    background: var(--card-white);
    display: flex;
    align-items: center;
    padding: 0 36px;
  }
  .identity {
    width: 200px;
    text-align: right;
    padding-right: 26px;
  }
  .identity__name {
    font-family: "Oswald", sans-serif;
    font-weight: 500;
    font-size: 34px;
    letter-spacing: 1px;
    color: var(--gold);
    line-height: 1.1;
  }
  .identity__title {
    font-family: "Montserrat", sans-serif;
    font-size: 13px;
    letter-spacing: 2px;
    color: var(--text-grey);
    margin-top: 4px;
  }
  .divider {
    width: 1px;
    height: 84px;
    background: var(--gold);
  }
  .contact {
    list-style: none;
    padding-left: 22px;
    font-family: "Montserrat", sans-serif;
    font-size: 11.5px;
    color: var(--text-grey);
    line-height: 1.55;
  }
  .contact__item { display: flex; align-items: flex-start; gap: 7px; }
  .contact__icon { width: 10px; height: 10px; margin-top: 4px; flex: none; }
  .card--front {
    background: var(--card-black);
    display: flex;
    flex-direction: column;
    align-items: center;
    justify-content: center;
  }
  .brand__mark {
    width: 70px; height: 70px;
    border-radius: 50%;
    border: 3px solid var(--silver);
    margin-bottom: 18px;
  }
  .brand__name {
    font-family: "Cinzel", serif;
    font-size: 34px;
    color: var(--silver);
    letter-spacing: 2px;
  }
  .brand__tagline {
    font-family: "Cinzel", serif;
    font-size: 13px;
    color: var(--silver);
    letter-spacing: 1.5px;
    margin-top: 10px;
  }
</style>
</head>
<body>
  <section class="card card--back">
    <div class="identity">
      <p class="identity__name">DANIEL BROOKS</p>
      <p class="identity__title">DIRECTOR</p>
    </div>
    <div class="divider"></div>
    <ul class="contact">
      <li class="contact__item">
        <svg class="contact__icon" viewBox="0 0 10 10"><path d="M5 0a3.5 3.5 0 0 0-3.5 3.5C1.5 6 5 10 5 10s3.5-4 3.5-6.5A3.5 3.5 0 0 0 5 0z" fill="#d4b44a"/><circle cx="5" cy="3.5" r="1.2" fill="#fff"/></svg>
        <span>3175 W. Calder Ave., Suite 842,<br>Fort Worth, TX 76142</span>
      </li>
      <li class="contact__item">
        <svg class="contact__icon" viewBox="0 0 10 10"><path d="M2 0.5l2 2-1 1.3a6 6 0 0 0 3.2 3.2l1.3-1 2 2-1.4 1.5C4.5 9.5 0.5 5.5 0.5 2z" fill="#d4b44a"/></svg>
        <span>(214) 738-2956</span>
      </li>
      <li class="contact__item">
        <svg class="contact__icon" viewBox="0 0 10 10"><rect x="0.5" y="1.5" width="9" height="7" fill="none" stroke="#d4b44a"/><path d="M0.5 1.5L5 5.5l4.5-4" fill="none" stroke="#d4b44a"/></svg>
        <span>info@willowmeretherapy.example</span>
      </li>
      <li class="contact__item">
        <svg class="contact__icon" viewBox="0 0 10 10"><circle cx="5" cy="5" r="4.5" fill="none" stroke="#d4b44a"/><ellipse cx="5" cy="5" rx="2" ry="4.5" fill="none" stroke="#d4b44a"/><path d="M0.5 5h9" stroke="#d4b44a"/></svg>
        <span>www.WillowmereTherapy.example</span>
      </li>
    </ul>
  </section>

  <section class="card card--front">
    <div class="brand__mark"></div>
    <p class="brand__name">WILLOWMERE THERAPY</p>
    <p class="brand__tagline">ENDURE - RENEW - FLOURISH</p>
  </section>
</body>
</html>
```